we can communicate on this, but i want to follow the approach we took on Pell|Quorn & Tillet but i feel the card front needs the black background and the platinum and gold logo. The back? I am open. we can use the same info from PQ&T. Vellum Crest is an enhanced equity investment fund - basically a very exclusive boutique hedge fund that uses only stock options. very advanced things. hope you are interested

Contact Information for Business Card

Dr. Owen T. Brisket, CFA
Scientifique de fusée financière
555.014.2296
TheDoc4793@mailvessel.example

4718 Fennel Brook Way N.
West Fargo, ND 58078

No web site

Colors

Designer to choose colors to be used in the design.

Requirements
Nice to have
• I tend to prefer the most visible applications of the logo to include logo and name, the logo version with a black background and the gold and platinum components separated by the black. I see this working well for a single side (logo and name - this is card front to me).
• I am fairly open to other treatments on the reverse side with the data. To me, it makes sense to have a different color rendition of the logo on the reverse and it may be a muted black tone on tone or an oversized portion that would have spot UV. Or, the reverse may play with colors and layout
Should not have
• Other colors = no no
• Decorative font

```html
<!DOCTYPE html>
<html lang="en">
<head>
<meta charset="utf-8">
<title>Vellum Crest — Business Card</title>
<link href="https://fonts.googleapis.com/css2?family=Roboto:ital,wght@0,400;0,500;0,700;1,400&display=swap" rel="stylesheet">
<style>
  :root {
    --stage: #1d1d1e;
    --card-black: #1a1a1b;
    --card-white: #ffffff;
    --gold: #c9a227;
    --gold-soft: #e6d49a;
    --platinum: #9c9c9c;
    --ink: #141414;
    --text-grey: #4a4a4a;
  }
  * { box-sizing: border-box; margin: 0; padding: 0; }
  html, body {
    width: 1200px; height: 800px; overflow: hidden;
    background: var(--stage);
    font-family: "Roboto", Arial, sans-serif;
  }
  .canvas { position: relative; width: 1200px; height: 800px; }

  .card {
    position: absolute;
    width: 560px; height: 320px;
    box-shadow: 0 10px 30px rgba(0,0,0,.45);
  }

  /* Front: black card */
  .card--front {
    left: 250px; top: 60px;
    background: var(--card-black);
  }
  .front__mark {
    position: absolute; left: 50%; top: 70px;
    transform: translateX(-50%);
    width: 128px; height: 128px; border-radius: 50%;
    background: linear-gradient(135deg, #8d8d8d 0%, #5a5a5a 55%, #2a2a2a 100%);
  }
  .front__name {
    position: absolute; left: 0; right: 0; top: 222px;
    text-align: center;
    font-weight: 500; font-size: 22px; letter-spacing: 4px;
    text-transform: uppercase;
    color: var(--platinum);
  }

  /* Back: white card */
  .card--back {
    left: 390px; top: 420px;
    background: var(--card-white);
  }
  .brand {
    position: absolute; right: 34px; top: 30px;
    display: flex; align-items: center; gap: 12px;
  }
  .brand__dot {
    width: 40px; height: 40px; border-radius: 50%;
    background: var(--gold);
  }
  .brand__name {
    font-weight: 700; font-size: 22px; letter-spacing: 1px;
    text-transform: uppercase; color: var(--ink);
  }

  .details { position: absolute; left: 44px; top: 150px; width: 340px; }
  .person__name {
    color: var(--gold); font-weight: 500; font-size: 22px; line-height: 1;
  }
  .person__name .honorific { font-size: 15px; }
  .person__name .credential { font-size: 12px; vertical-align: 6px; }
  .person__title {
    margin-top: 5px;
    font-style: italic; font-size: 12.5px; color: var(--text-grey);
  }
  .rule {
    height: 1px; background: var(--gold-soft); margin: 10px 0;
  }
  .contact { list-style: none; }
  .contact__item {
    display: flex; align-items: center; gap: 10px;
    font-size: 12.5px; color: var(--text-grey); line-height: 17px;
    white-space: nowrap;
  }
  .contact__icon { width: 12px; height: 12px; flex: none; fill: var(--gold); }
</style>
</head>
<body>
<main class="canvas">

  <section class="card card--front" aria-label="Card front">
    <div class="front__mark"></div>
    <p class="front__name">Vellum Crest</p>
  </section>

  <section class="card card--back" aria-label="Card back">
    <div class="brand">
      <span class="brand__dot"></span>
      <span class="brand__name">Vellum Crest</span>
    </div>

    <div class="details">
      <h1 class="person__name"><span class="honorific">Dr.</span> Owen T. Brisket, <span class="credential">CFA</span></h1>
      <p class="person__title">Scientifique de fusée financière</p>
      <div class="rule"></div>

      <ul class="contact">
        <li class="contact__item">
          <svg class="contact__icon" viewBox="0 0 12 12"><path d="M3 0h6a1 1 0 0 1 1 1v10a1 1 0 0 1-1 1H3a1 1 0 0 1-1-1V1a1 1 0 0 1 1-1zm0 1.5v8h6v-8z"/></svg>
          555.014.2296
        </li>
        <li class="contact__item">
          <svg class="contact__icon" viewBox="0 0 12 12"><path d="M0 2h12v8H0z M1 3l5 3.5L11 3v-.2H1z" fill-rule="evenodd"/></svg>
          TheDoc4793@mailvessel.example
        </li>
      </ul>

      <div class="rule"></div>

      <ul class="contact contact--address">
        <li class="contact__item">
          <svg class="contact__icon" viewBox="0 0 12 12"><path d="M6 0a4 4 0 0 1 4 4c0 3-4 8-4 8S2 7 2 4a4 4 0 0 1 4-4zm0 2.3a1.7 1.7 0 1 0 0 3.4 1.7 1.7 0 0 0 0-3.4z"/></svg>
          4718 Fennel Brook Way N., West Fargo, ND 58078
        </li>
      </ul>
    </div>
  </section>

</main>
</body>
</html>
```